Graphic Design for Application Form and Menu

We are a success education company called Tandem Crestline. We are designing a USB application for a personal development program that will be cross platform (PC/Mac). The product is called Quiet Harvest, Meridale Academy (These logos are already created). The program will open pdf books in a Flash reader, play audio and video files in the default media player, and open windows for recording entries in a journal and for setting goals.
We need a graphic design for a small control panel (300px X 300px) to launch the different modules of the program.

We are looking for a design that is clean and professional.
A sample is included of everything that needs to be on the form. A sample menu is also included. We are looking for other designs for the form and menu.
Updates

Industry/Entity Type

Graphic Design

Requirements
Must have
• The panel will have: a menu, two toolbars, and two status panels.
ItemDetails:
A menu will have items for "Welcome, Profile, and Kudos."
One tool bar will have items for "Guidebooks (w/9 item popup menu), Audios (w/9 item popup menu), Videos (w/9 item popup menu), Journal (w/2 item popup menu), and Goals."
A second tool bar will have items for "Blog, Community, Events, Sovereignty, Foundation, and Influence."
The tool bars should have icons and text.
There should be two status panel, one for Audio and one for Video.
The status panels should show the name of the audio or video that is opened, have check boxes for: Add to favorites, Come back, and Done, and have links for: Audios, Top Posts, Post, and Tips.

```html
<!DOCTYPE html>
<html lang="en">
<head>
<meta charset="utf-8">
<title>Tandem Crestline — Quiet Harvest Control Panel</title>
<link rel="stylesheet" href="https://fonts.googleapis.com/css2?family=Open+Sans:wght@400;600;700&display=swap">
<style>
:root{
  --bg:#e9eef0;
  --dark:#3a3a3a;
  --dark-2:#2c2c2c;
  --teal:#3aa3bb;
  --teal-light:#63b8cc;
  --tab-white:#ffffff;
  --content:#e3eef1;
  --card:#f7fafb;
  --card-border:#c8dde4;
  --grey-text:#8a8a8a;
  --name-bg:#dcdcdc;
  --name-text:#666666;
  --label:#555555;
  --link-bg:#86c8f2;
  --link-bg-dark:#6ab7e8;
  --white:#ffffff;
  --icon-grey:#a9a9a9;
}
*{box-sizing:border-box;margin:0;padding:0}
html,body{width:1200px;height:699px;overflow:hidden}
body{background:var(--bg);font-family:"Open Sans",Arial,sans-serif;position:relative}
.stage{position:absolute;left:355px;top:111px;width:300px;height:293px;transform:scale(1.633);transform-origin:0 0}
.panel{width:300px;height:293px;background:var(--dark);position:relative;box-shadow:0 3px 10px rgba(0,0,0,.35)}
.menu{position:absolute;left:10px;top:3px;display:flex;gap:4px}
.menu-tab{height:22px;padding:0 10px;font-size:11.5px;font-weight:700;line-height:23px;color:var(--white);background:var(--teal)}
.menu-tab.is-active{background:var(--tab-white);color:var(--dark-2)}
.menu-tab.profile{width:68px;text-align:center}
.menu-tab.kudos{width:69px;text-align:center}
.content{position:absolute;left:0;top:25px;width:300px;height:220px;background:var(--content);border-top:5px solid var(--white)}
.content::after{content:"";position:absolute;left:0;bottom:-8px;width:300px;height:6px;background:var(--white)}
.toolbar{position:absolute;left:10px;top:10px;width:280px;height:40px;background:var(--white);border-radius:8px;border:1px solid #d7e3e6;display:flex;justify-content:space-around;align-items:center;padding:0 6px}
.tool{display:flex;flex-direction:column;align-items:center;gap:2px;width:50px}
.tool svg{width:22px;height:20px}
.tool-label{font-size:5.5px;color:var(--grey-text);text-transform:uppercase;letter-spacing:.2px}
.tool.is-active .tool-label{color:var(--teal)}
.status{position:absolute;top:63px;width:136px;height:139px;background:var(--card);border:1px solid var(--card-border);border-radius:8px;overflow:hidden}
.status.audio{left:10px}
.status.video{left:154px}
.status-title{height:22px;background:linear-gradient(#6fc0d3,var(--teal-light));color:var(--white);font-size:11px;font-weight:700;text-align:center;line-height:22px;border-radius:8px 8px 0 0}
.now-playing{margin:6px 5px 4px;height:18px;background:var(--name-bg);color:var(--name-text);font-size:10px;text-align:center;line-height:18px;border-radius:2px}
.checks{list-style:none;padding:0 6px}
.check{display:flex;align-items:center;gap:6px;height:15px;font-size:8.5px;color:var(--label)}
.box{width:11px;height:11px;border:1px solid #9fb9c2;background:linear-gradient(#ffffff,#e4eef2);border-radius:2px;position:relative}
.box svg{position:absolute;left:-1px;top:-4px;width:14px;height:14px}
.links{display:grid;grid-template-columns:1fr 1fr;gap:4px 5px;padding:5px 5px 0}
.link{height:14px;background:linear-gradient(var(--link-bg),var(--link-bg-dark));color:var(--white);font-size:8.5px;font-weight:700;text-align:center;line-height:14px;border-radius:2px}
.footer-bar{position:absolute;left:0;top:253px;width:300px;height:40px;display:flex;justify-content:space-around;align-items:center;padding:0 10px}
.footer-item{display:flex;flex-direction:column;align-items:center;gap:2px;width:44px}
.footer-item svg{width:22px;height:18px}
.footer-label{font-size:4.8px;font-weight:700;color:var(--white);text-transform:uppercase}
</style>
</head>
<body>
<div class="stage">
  <section class="panel" aria-label="Quiet Harvest control panel">
    <nav class="menu">
      <div class="menu-tab is-active">Welcome</div>
      <div class="menu-tab profile">Profile</div>
      <div class="menu-tab kudos">Kudos</div>
    </nav>

    <div class="content">
      <div class="toolbar">
        <div class="tool">
          <svg viewBox="0 0 24 20"><path d="M2 3h8c1 0 2 1 2 2v13c0-1-1-2-2-2H2z M22 3h-8c-1 0-2 1-2 2v13c0-1 1-2 2-2h8z" fill="none" stroke="var(--icon-grey)" stroke-width="1.4"/></svg>
          <span class="tool-label">Guidebook</span>
        </div>
        <div class="tool is-active">
          <svg viewBox="0 0 24 20"><path d="M4 14v-3a8 8 0 0 1 16 0v3" fill="none" stroke="var(--teal)" stroke-width="2"/><rect x="3" y="12" width="4" height="7" rx="1.5" fill="var(--teal)"/><rect x="17" y="12" width="4" height="7" rx="1.5" fill="var(--teal)"/></svg>
          <span class="tool-label">Audio</span>
        </div>
        <div class="tool">
          <svg viewBox="0 0 24 20"><rect x="2" y="4" width="14" height="12" rx="1" fill="var(--icon-grey)"/><path d="M16 9l6-4v10l-6-4z" fill="var(--icon-grey)"/></svg>
          <span class="tool-label">Video</span>
        </div>
        <div class="tool">
          <svg viewBox="0 0 24 20"><rect x="5" y="0" width="14" height="20" fill="var(--icon-grey)"/><rect x="7" y="0" width="2" height="20" fill="#cfcfcf"/></svg>
          <span class="tool-label">Journal</span>
        </div>
        <div class="tool">
          <svg viewBox="0 0 24 20"><rect x="2" y="2" width="20" height="16" fill="none" stroke="var(--icon-grey)" stroke-width="1.4"/><path d="M4 14l5-5 4 3 6-6" fill="none" stroke="var(--icon-grey)" stroke-width="1.4"/></svg>
          <span class="tool-label">Goals</span>
        </div>
      </div>

      <article class="status audio">
        <h2 class="status-title">Audio</h2>
        <div class="now-playing">Departure 1</div>
        <ul class="checks">
          <li class="check"><span class="box"><svg viewBox="0 0 14 14"><path d="M2 8l3 4 8-11" fill="none" stroke="#3d7f96" stroke-width="2.2"/></svg></span>Come back</li>
          <li class="check"><span class="box"></span>Done</li>
          <li class="check"><span class="box"></span>Add to favourites</li>
        </ul>
        <div class="links">
          <span class="link">Audios</span><span class="link">Top Posts</span>
          <span class="link">Tips</span><span class="link">Post</span>
        </div>
      </article>

      <article class="status video">
        <h2 class="status-title">Video</h2>
        <div class="now-playing">Departure 1</div>
        <ul class="checks">
          <li class="check"><span class="box"><svg viewBox="0 0 14 14"><path d="M2 8l3 4 8-11" fill="none" stroke="#3d7f96" stroke-width="2.2"/></svg></span>Come back</li>
          <li class="check"><span class="box"></span>Done</li>
          <li class="check"><span class="box"></span>Add to favourites</li>
        </ul>
        <div class="links">
          <span class="link">Audios</span><span class="link">Top Posts</span>
          <span class="link">Tips</span><span class="link">Post</span>
        </div>
      </article>
    </div>

    <nav class="footer-bar">
      <div class="footer-item">
        <svg viewBox="0 0 24 20"><path d="M2 3h8c1 0 2 1 2 2v13c0-1-1-2-2-2H2z M22 3h-8c-1 0-2 1-2 2v13c0-1 1-2 2-2h8z" fill="none" stroke="var(--white)" stroke-width="1.6"/></svg>
        <span class="footer-label">Blog</span>
      </div>
      <div class="footer-item">
        <svg viewBox="0 0 24 20"><path d="M4 14v-3a8 8 0 0 1 16 0v3" fill="none" stroke="var(--white)" stroke-width="2"/><rect x="3" y="12" width="4" height="7" rx="1.5" fill="var(--white)"/><rect x="17" y="12" width="4" height="7" rx="1.5" fill="var(--white)"/></svg>
        <span class="footer-label">Community</span>
      </div>
      <div class="footer-item">
        <svg viewBox="0 0 24 20"><rect x="2" y="4" width="14" height="12" rx="1" fill="var(--white)"/><path d="M16 9l6-4v10l-6-4z" fill="var(--white)"/></svg>
        <span class="footer-label">Events</span>
      </div>
      <div class="footer-item">
        <svg viewBox="0 0 24 20"><rect x="5" y="0" width="14" height="20" fill="var(--white)"/><rect x="7" y="0" width="2" height="20" fill="var(--dark)"/></svg>
        <span class="footer-label">Sovereignty</span>
      </div>
      <div class="footer-item">
        <svg viewBox="0 0 24 20"><rect x="2" y="2" width="20" height="16" fill="none" stroke="var(--white)" stroke-width="1.6"/><path d="M4 14l5-5 4 3 6-6" fill="none" stroke="var(--white)" stroke-width="1.6"/></svg>
        <span class="footer-label">Foundation</span>
      </div>
      <div class="footer-item">
        <svg viewBox="0 0 24 20"><path d="M2 3h8c1 0 2 1 2 2v13c0-1-1-2-2-2H2z M22 3h-8c-1 0-2 1-2 2v13c0-1 1-2 2-2h8z" fill="none" stroke="var(--white)" stroke-width="1.6"/></svg>
        <span class="footer-label">Influence</span>
      </div>
    </nav>
  </section>
</div>
</body>
</html>
```